BrightPathLink (Post-Prison Reentry & Aftercare)
Business Cards, Letterhead, Envelopes, Fax Cover Sheet, Email Signature, Powerpoint Template
I need double sided standard sized Business Card [3.5" x 2"]
Amasis MT Std
Professional
Bram Cadley
PO Box 48392
Harrowmere, MN 55990
bram@ourbrightpathlink.example
www.ourbrightpathlink.example

```html
<!DOCTYPE html>
<html lang="en">
<head>
<meta charset="utf-8">
<title>BrightPathLink Business Card</title>
<link href="https://fonts.googleapis.com/css2?family=Montserrat:wght@500;800&family=Roboto+Slab:wght@400;600&display=swap" rel="stylesheet">
<style>
  :root {
    --bg: #e9e6e2;
    --card: #ffffff;
    --ink: #231f20;
    --red: #d42a2f;
    --grey: #6d6e71;
    --rule: #e4e4e4;
  }
  * { margin: 0; padding: 0; box-sizing: border-box; }
  html, body { width: 1200px; height: 629px; overflow: hidden; }
  body {
    background: var(--bg);
    display: flex;
    align-items: center;
    justify-content: center;
    gap: 60px;
    font-family: "Roboto Slab", serif;
  }
  .card {
    width: 511px;
    height: 292px;
    background: var(--card);
    box-shadow: 0 6px 18px rgba(0,0,0,.18);
    position: relative;
    overflow: hidden;
  }
  .brand {
    display: flex;
    align-items: center;
    gap: 12px;
  }
  .brand-dot {
    width: 34px; height: 34px;
    border-radius: 50%;
    background: var(--ink);
    flex: none;
  }
  .brand-name {
    font-family: "Montserrat", sans-serif;
    font-weight: 800;
    font-size: 30px;
    letter-spacing: -0.5px;
    color: var(--ink);
    line-height: 1;
    text-transform: uppercase;
    white-space: nowrap;
  }
  .brand-tagline {
    font-family: "Montserrat", sans-serif;
    font-weight: 500;
    font-size: 8px;
    letter-spacing: 1.6px;
    color: var(--grey);
    text-transform: uppercase;
    margin-top: 4px;
    white-space: nowrap;
  }
  .card-front { display: flex; align-items: center; justify-content: center; }

  .card-back .back-top {
    height: 120px;
    display: flex;
    align-items: center;
    justify-content: center;
    border-bottom: 1px solid var(--rule);
  }
  .card-back .brand-name { font-size: 26px; }
  .card-back .brand-dot { width: 30px; height: 30px; }
  .back-bottom {
    position: absolute;
    left: 0; right: 0; bottom: 0;
    height: 172px;
    background: var(--red);
    color: #fff;
    display: flex;
    padding: 30px 36px;
  }
  .holder {
    flex: 1;
    text-align: center;
    font-size: 11px;
    line-height: 1.55;
    border-right: 1px solid rgba(255,255,255,.45);
    padding-right: 20px;
    white-space: nowrap;
  }
  .holder-name { font-weight: 600; font-size: 13px; }
  .holder-role { margin-bottom: 12px; }
  .contacts {
    flex: 1.25;
    list-style: none;
    padding-left: 22px;
    font-size: 10.5px;
    line-height: 1.9;
    white-space: nowrap;
  }
  .contacts li { display: flex; align-items: center; gap: 8px; }
  .contacts svg { width: 11px; height: 11px; flex: none; }
</style>
</head>
<body>

  <section class="card card-front">
    <div class="brand">
      <span class="brand-dot"></span>
      <div>
        <div class="brand-name">BrightPathLink</div>
        <div class="brand-tagline">Post-Prison Reentry and Aftercare</div>
      </div>
    </div>
  </section>

  <section class="card card-back">
    <div class="back-top">
      <div class="brand">
        <span class="brand-dot"></span>
        <div>
          <div class="brand-name">BrightPathLink</div>
          <div class="brand-tagline">Post-Prison Reentry and Aftercare</div>
        </div>
      </div>
    </div>
    <div class="back-bottom">
      <div class="holder">
        <div class="holder-name">Bram Cadley</div>
        <div class="holder-role">Executive Director</div>
        <div>PO Box 48392</div>
        <div>Harrowmere, MN 55990</div>
      </div>
      <ul class="contacts">
        <li><svg viewBox="0 0 12 12"><path d="M3 1l2 2.5-1 1.2a7 7 0 0 0 3.3 3.3l1.2-1L11 9l-1 2C5 11 1 7 1 2z" fill="#fff"/></svg>(612) 555-0147</li>
        <li><svg viewBox="0 0 12 12"><rect x="2" y="1" width="8" height="4" fill="none" stroke="#fff"/><rect x="1" y="5" width="10" height="6" fill="#fff"/></svg>(612) 555-0182</li>
        <li><svg viewBox="0 0 12 12"><rect x="3" y="0.5" width="6" height="11" rx="1" fill="none" stroke="#fff"/><circle cx="6" cy="9.5" r=".8" fill="#fff"/></svg>(612) 555-0139</li>
        <li><svg viewBox="0 0 12 12"><rect x="0.5" y="2.5" width="11" height="7" fill="none" stroke="#fff"/><path d="M.5 2.5L6 7l5.5-4.5" fill="none" stroke="#fff"/></svg>bram@ourbrightpathlink.example</li>
        <li><svg viewBox="0 0 12 12"><circle cx="6" cy="6" r="5.2" fill="none" stroke="#fff"/><path d="M.8 6h10.4M6 .8c-3 3-3 7.4 0 10.4M6 .8c3 3 3 7.4 0 10.4" fill="none" stroke="#fff" stroke-width=".8"/></svg>www.ourbrightpathlink.example</li>
      </ul>
    </div>
  </section>

</body>
</html>
```